Fernbrook Pet Showcase Ticket Card Design

We’re looking to create a complimentary “ticket” card for Fernbrook Pet Showcase that can be handed out physically. We host an event for cat lovers. The card should feel special and collectible. Size will be a standard business card (3.5" x 2") Orientation is open to designer recommendation. This ticket will be used as a complimentary entry pass for select guests, partners, & giveaways. Key elements to Include are the Fernbrook Pet Showcase logo (provided), the words “Complimentary Ticket” or similar wording (open to creative phrasing and cat puns) A blank space for the Event date (to be written in) & Ticket number (to be written in) . Event Name is always "Fernbrook Pet Bazaar & Rehoming Day". We want the ticket to feel clean & modern but slightly playful with a cat-inspired touch (think clever, not kitschy). Could include a subtle cat motif or texture (e.g., whisker lines, paw detail, soft patterning) Open to unique layout ideas that still leave clear writing space. Avoid overcrowding of elements. Ticket should also have fine print "This ticket is not redeemable for cash and cannot be combined with any other offers or discounts, can only be used for the date indicated"

Target Market(s)

Women

Industry/Entity Type

pets

Colors
6B429C
8869AF
B7A5CE
E3DAEB
F3F0F8

Requirements
Must have
• Fernbrook Pet Showcase Logo & words around complimentary ticket as well as the fine print
Nice to have
• cat-inspired touch (think clever, not kitschy). Could include a subtle cat motif or texture (e.g., whisker lines, paw detail, soft patterning)
Should not have
• should not look cartoony

```html
<!DOCTYPE html>
<html lang="en">
<head>
<meta charset="utf-8">
<title>Fernbrook Pet Showcase – Guest Ticket</title>
<link href="https://fonts.googleapis.com/css2?family=Montserrat:wght@400;600&family=Dancing+Script:wght@600&display=swap" rel="stylesheet">
<style>
  :root {
    --backdrop: #e6e6e8;
    --card-navy: #23263d;
    --cream: #f3d9c6;
    --rule: #c9b6aa;
    --paw-grey: #55576b;
  }
  html, body {
    margin: 0;
    width: 1200px;
    height: 965px;
    overflow: hidden;
    background: var(--backdrop);
  }
  .ticket-card {
    position: absolute;
    left: 75px;
    top: 182px;
    width: 1050px;
    height: 600px;
    background: var(--card-navy);
    color: var(--cream);
    font-family: "Montserrat", sans-serif;
    box-shadow: 0 18px 40px rgba(0,0,0,0.18);
  }
  .frame {
    position: absolute;
    inset: 0;
    width: 1050px;
    height: 600px;
  }
  .brand-name {
    position: absolute;
    left: 64px;
    top: 64px;
    width: 230px;
    font-weight: 600;
    font-size: 34px;
    line-height: 1.08;
    color: var(--cream);
  }
  .brand-mark {
    display: inline-block;
    width: 14px;
    height: 14px;
    border-radius: 50%;
    background: var(--cream);
    margin-left: 6px;
    vertical-align: middle;
  }
  .event-name {
    position: absolute;
    left: 320px;
    top: 74px;
    font-size: 30px;
    font-weight: 400;
    line-height: 1.2;
  }
  .divider {
    position: absolute;
    left: 64px;
    top: 196px;
    width: 800px;
    height: 1.5px;
    background: linear-gradient(90deg, var(--rule), rgba(201,182,170,0.35));
  }
  .whisker-art {
    position: absolute;
    right: 90px;
    top: 52px;
    width: 170px;
    height: 120px;
    background: radial-gradient(ellipse at center, rgba(243,217,198,0.35), rgba(243,217,198,0.05));
    border-radius: 10px;
  }
  .paw-trail {
    position: absolute;
    background: linear-gradient(180deg, rgba(85,87,107,0.55), rgba(85,87,107,0.25));
    border-radius: 12px;
  }
  .paw-trail--right { right: 48px; top: 200px; width: 90px; height: 220px; }
  .paw-trail--left { left: 56px; top: 290px; width: 110px; height: 230px; }
  .ticket-title {
    position: absolute;
    left: 300px;
    top: 200px;
    font-family: "Dancing Script", cursive;
    font-weight: 600;
    font-size: 80px;
    line-height: 1;
  }
  .write-in {
    position: absolute;
    left: 190px;
    display: flex;
    align-items: flex-end;
    font-size: 30px;
  }
  .write-in .blank {
    flex: 1;
    margin-left: 14px;
    margin-bottom: 7px;
    border-bottom: 1.5px solid var(--rule);
  }
  .write-in--date { top: 322px; width: 690px; }
  .write-in--number { top: 398px; width: 790px; }
  .fine-print {
    position: absolute;
    left: 190px;
    top: 468px;
    width: 800px;
    font-size: 19px;
    line-height: 1.3;
    text-align: center;
  }
</style>
</head>
<body>
  <div class="ticket-card">
    <svg class="frame" viewBox="0 0 1050 600" aria-hidden="true">
      <rect x="22" y="22" width="1006" height="556" fill="none" stroke="#f3d9c6" stroke-width="2"/>
      <rect x="32" y="32" width="986" height="536" fill="none" stroke="#f3d9c6" stroke-width="1"/>
    </svg>

    <div class="brand-name">Fernbrook<br>Pet Showcase<span class="brand-mark"></span></div>

    <div class="event-name">Fernbrook Pet Bazaar<br>&amp; Rehoming Day</div>

    <div class="divider"></div>

    <div class="whisker-art" role="img" aria-label="Line drawing of cat ears and whiskers"></div>

    <div class="paw-trail paw-trail--right" role="img" aria-label="Faint trail of paw prints"></div>
    <div class="paw-trail paw-trail--left" role="img" aria-label="Faint trail of paw prints"></div>

    <div class="ticket-title">Meow Guest Ticket</div>

    <div class="write-in write-in--date"><span>Event Date:</span><span class="blank"></span></div>
    <div class="write-in write-in--number"><span>Ticket No :</span><span class="blank"></span></div>

    <p class="fine-print">This ticket is not redeemable for cash and cannot be combined with any other offers or discounts, can only be used for the date indicated</p>
  </div>
</body>
</html>
```